Illustrated cover for unique non-fiction book (paperback & eBook)

I know the image I want on my book covers (eBook and paperback) but I need you to come up with the style and treatment. I am a self-publisher and my book is about the human obsession with being better than animals, even though scientists keep telling us there’s no evidence to support it. To illustrate how illogical it is I want to show a see-saw. On the end that is down (left) sits a man, and on the end that is up (right) sits a whole bunch of large and small animals that should outweigh him but don’t. Birds on heads and shoulders etc. Title: 'Notes Toward a Quieter Ladder'; author’s name: Derek Moffanby. The style should be modern, uncluttered and probably not too realistic (I don’t want a cartoon style since the content of the book is pretty serious). No strong colour preferences at this stage, just needs to be eye-catching with good contrast. Perhaps a plain white background might work. Dimensions: 215 x 135mm, 374 pages, imprint: Pellingrove Press. Back page text is attached. [NOTE: If you feel you could express this illogicality in a completely different way please feel free to submit a draft design.]

Target Market(s)

General readers, particularly those interested in social sciences/life sciences.

Industry/Entity Type

Publishing

Requirements
Must have
• Good impact, clearly showing the absurdity of our attitude towards other species.
Nice to have
• Suggestthat the book is interesting and challenging.
Should not have
• Not cluttered or difficult to readthe image.

```html
<!DOCTYPE html>
<html lang="en">
<head>
<meta charset="utf-8">
<title>Notes Toward a Quieter Ladder — Cover</title>
<link href="https://fonts.googleapis.com/css2?family=Cinzel:wght@400;600&family=Crimson+Pro:ital,wght@0,400;0,600;1,400&display=swap" rel="stylesheet">
<style>
  :root {
    --navy: #333a45;
    --navy-deep: #2c323c;
    --cream: #ebe8e5;
    --paper: #f3f2f4;
    --rust: #7a3b3b;
    --ink: #2b313b;
    --art: #d9d6d3;
  }
  * { margin: 0; padding: 0; box-sizing: border-box; }
  html, body { width: 982px; height: 1200px; overflow: hidden; }
  body { background: var(--paper); position: relative; }

  .jacket {
    position: absolute; left: 26px; top: 257px; width: 930px; height: 685px;
    display: flex;
  }

  /* Back cover */
  .back {
    position: relative; width: 430px; height: 100%;
    background: var(--navy); color: var(--cream);
    padding: 38px 30px 0;
    font-family: "Crimson Pro", serif;
  }
  .back-title {
    text-align: center; font-family: "Cinzel", serif; line-height: 1.1;
    font-weight: 400;
  }
  .back-title .small { display: block; font-size: 16px; }
  .back-title .large { display: block; font-size: 25px; }
  .back-lead {
    margin-top: 12px; padding: 10px 12px;
    background: var(--cream); color: var(--ink);
    font-size: 13.5px; font-weight: 600; line-height: 1.3; text-align: justify;
  }
  .back-body {
    margin-top: 14px; font-size: 11.5px; line-height: 1.35; text-align: justify;
  }
  .back-body p + p { margin-top: 9px; }
  .back-rule {
    margin: 14px auto 0; width: 200px; height: 1px; background: var(--rust);
  }
  .back-heading {
    margin-top: 10px; text-align: center; font-size: 14px; font-weight: 600;
  }
  .back-bio {
    margin-top: 6px; font-size: 11.5px; line-height: 1.35; text-align: justify;
  }

  /* Spine */
  .spine {
    position: relative; width: 70px; height: 100%;
    background: var(--cream);
  }
  .spine-top {
    position: absolute; left: 0; top: 0; width: 100%; height: 300px;
    background: var(--navy);
  }
  .spine-author, .spine-title {
    position: absolute; left: 50%; white-space: nowrap;
    font-family: "Cinzel", serif;
    transform: translate(-50%, -50%) rotate(90deg);
  }
  .spine-author { top: 150px; color: var(--cream); font-size: 19px; letter-spacing: 0.5px; }
  .spine-title { top: 465px; text-align: center; line-height: 1.1; }
  .spine-title .small { display: block; color: var(--ink); font-size: 15px; }
  .spine-title .large { display: block; color: var(--rust); font-size: 21px; font-weight: 600; }
  .imprint {
    position: absolute; bottom: 14px; left: 0; width: 100%; text-align: center;
    font-family: "Cinzel", serif; font-size: 8px; line-height: 1.2; color: var(--ink);
  }

  /* Front cover */
  .cover {
    position: relative; width: 430px; height: 100%;
    background: var(--cream);
  }
  .cover-top {
    position: absolute; left: 0; top: 0; width: 100%; height: 300px;
    background: var(--navy);
  }
  .title {
    position: absolute; right: 24px; top: 70px; text-align: right;
    font-family: "Cinzel", serif; color: var(--cream); line-height: 1;
  }
  .title-lead { display: block; font-size: 28px; letter-spacing: 0.5px; }
  .title-main { display: block; font-size: 68px; font-weight: 600; margin-top: 4px; }
  .title-box {
    display: inline-block; margin-top: 6px; padding: 6px 14px 5px;
    background: var(--cream); color: var(--navy); font-size: 44px; font-weight: 600;
  }
  .rule {
    position: absolute; left: 26px; top: 255px; width: 5px; height: 400px;
    background: var(--rust);
  }
  .artwork { position: absolute; left: 0; top: 0; }
  .subtitle {
    position: absolute; left: 46px; top: 380px; z-index: 1;
    font-family: "Crimson Pro", serif; font-style: italic; font-size: 21px;
    line-height: 1.15; color: var(--ink);
  }
  .subtitle em { font-style: italic; border-bottom: 1.5px solid var(--rust); }
  .author {
    position: absolute; left: 0; width: 100%; bottom: 26px; text-align: center;
    font-family: "Cinzel", serif; font-size: 23px; font-weight: 600;
    letter-spacing: 1px; color: var(--ink);
  }
</style>
</head>
<body>
  <div class="jacket">
    <section class="back">
      <h2 class="back-title">
        <span class="small">Notes Toward a</span>
        <span class="large">Quieter Ladder</span>
      </h2>
      <p class="back-lead">We have a paradox. Nowadays, we mistrust ideas relating to class, gender, race and nationality, yet we still embrace human supremacy, the belief that our species is superior and set apart. Trouble is, scientists find no evidence to support it. So why do we still insist on it?</p>
      <div class="back-body">
        <p>This is a place-in-nature book for the modern reader. Older classics were long a favourite, establishing the beliefs that shaped our outlook for generations. But those ideas were of their time. When we read them today we notice the pomposity and the sheer sense of entitlement. They are light on evidence and heavy on self-congratulation. It’s time to revisit the question with complete honesty. Think how satisfying it will be to have answers we can finally trust.</p>
        <p>By joining this mind quest you will discover the reasons we feel different. Not the promotional reasons, or the selective ones, or the shared delusions, but the real reasons. The answers, not always flattering, are waiting inside. It’s an investigation that will help you reach a startling conclusion.</p>
      </div>
      <div class="back-rule"></div>
      <h3 class="back-heading">About the Author</h3>
      <p class="back-bio">After a career as a senior analyst in the IT sector, Derek turned to the subject that had always struck him as illogical – man’s view of himself. A lifetime of interest in the sciences taught him that the big picture is too often neglected while academics pursue their own avenues of research. So he set about integrating many of these fields of study in a single quest for understanding. The project was successful, uncovering a hidden and unexpected reality. It is this he now wishes to share.</p>
    </section>

    <div class="spine">
      <div class="spine-top"></div>
      <div class="spine-author">Derek Moffanby</div>
      <div class="spine-title">
        <span class="small">Notes Toward a</span>
        <span class="large">Quieter Ladder</span>
      </div>
      <div class="imprint">PELLINGROVE<br>PRESS</div>
    </div>

    <section class="cover">
      <div class="cover-top"></div>
      <h1 class="title">
        <span class="title-lead">NOTES TOWARD A</span>
        <span class="title-main">QUIETER</span>
        <span class="title-box">LADDER</span>
      </h1>
      <div class="rule"></div>
      <svg class="artwork" width="430" height="685" viewBox="0 0 430 685" role="img"
           aria-label="Ink illustration of a see-saw: a seated man on the lowered left end outweighs a heap of animals — gorilla, elephant, snake, rhinos and a small bird — on the raised right end">
        <path d="M215 322 H412 V620 H40 V480 H215 Z" fill="var(--art)"/>
      </svg>
      <p class="subtitle">The <em>Real</em> Reasons<br>Why We Feel<br>Set Apart</p>
      <div class="author">DEREK MOFFANBY</div>
    </section>
  </div>
</body>
</html>
```